GUARANTEED WordPress design needed for a sassy, confident charisma coach!

We need a website design for Marla Penrick's brand new, responsive, Wordpress website.
Marla is a trainer / coach who teaches people how to be more charismatic and runs events, publishes video courses and has an ongoing video blog. Her old website is here: www.marlapenrick.co.uk ... but it's now time to have a much better site!
We have a strong idea about the technical components of the website, but we need a designer's eye to create a great style for the site (and provide layered PSD files which our developers will then convert to HTML and CSS).
Marla's brand is sassy, brave, warm and confident. The videos on her existing site give quite a good feel for her personality. We need a clean, stylish and compelling page that isn't too corporate and captures her personality. Every element needs to feel coherent, from fonts and headings to colours and spacing.
The following sites are not exactly what Marla wants (and certainly aren't right in terms of colours) but they give you an idea of the kind of people she is competing against and the area she is operating in:
http://www.tessa-broughley.example/
http://rowanfelsby.example/
Ideally, you will have done something similar and be able to key in on exactly the kind of thing we want: we're not looking to reinvent the wheel. Hopefully you won't mind tweaking a few things if you are close to what we need.
More detail is provided in the word document attached. But in a nutshell we need: a banner, footer, sign-up strap, menu bar, signature and 4 different basic page types. We want bursts of bright colours, contrasted with black and white if possible - sorry we can't be more specific than that...
The word doc also contains some amateur mock-ups as well (the images are also just mockups at this stage) - but although these give a general sense of the structure what we are looking for, we are clearly not designers...so please help! We need a designer's touch!
Kind regards,
Corin
PS The layered PSD versions of the mockup files are available on Cloudvantre: https://files.cloudvantre.example/sh/k72pqa4w1zbtmrd/QXvenlr8Ty3PwMiU6Hs2kYfDb?dl=0
Target Market(s)
Entrepreneurs who need to sell themselves.
Number of Pages Required
4 page

```html
<!DOCTYPE html>
<html lang="en">
<head>
<meta charset="utf-8">
<title>Marla Penrick — Attract, Connect, Influence</title>
<link rel="stylesheet" href="https://fonts.googleapis.com/css2?family=Lato:ital,wght@0,400;0,700;0,900;1,400;1,700;1,900&display=swap">
<style>
:root{
  --red:#e3202f;
  --red-dark:#b91522;
  --ink:#1e1e1e;
  --bar:#232323;
  --text:#555;
  --white:#fff;
  --coral:#ef5a47;
  --green:#2fa84a;
  --cyan:#1fb3e0;
}
*{box-sizing:border-box;margin:0;padding:0}
html,body{width:1200px;height:2256px;overflow:hidden}
body{position:relative;background:var(--white);font-family:'Lato',Arial,sans-serif;color:var(--ink)}
.abs{position:absolute}

/* top navigation */
.topbar{left:0;top:0;width:1200px;height:56px;background:var(--bar)}
.brand{left:232px;top:12px;color:var(--white);font-weight:700;font-size:26px;line-height:32px;display:flex;align-items:center;gap:10px}
.brand-dot{width:12px;height:12px;border-radius:50%;background:var(--red)}
.menu{left:564px;top:0;display:flex;height:56px}
.menu a{color:#ddd;text-decoration:none;font-size:12px;letter-spacing:.5px;padding:0 16px;line-height:60px;height:56px}
.menu a.active{background:var(--red);color:var(--white)}

/* hero */
.hero{left:0;top:56px;width:1200px;height:357px;background:linear-gradient(160deg,#fafafa 0%,#e9e9e9 35%,#fbfbfb 55%,#e4e4e4 80%,#f4f4f4 100%)}
.hero-word{right:618px;font-weight:900;font-size:54px;letter-spacing:1px;line-height:1;white-space:nowrap;text-align:right}
.hero-word.red{color:var(--red)}
.hero-rule{height:2px;background:var(--red)}
.hero-photo{left:660px;top:23px;width:186px;height:334px;background:linear-gradient(180deg,#c9a99a 0%,#d63a3f 45%,#c92a33 100%);border-radius:80px 80px 0 0}

/* signup strap */
.strap{left:0;top:413px;width:1200px;height:169px;background:linear-gradient(180deg,#f4f4f4,#dedede)}
.strap-black{left:0;top:582px;width:1200px;height:56px;background:#0d0d0d}
.monitor-screen{left:262px;top:419px;width:232px;height:150px;background:#141414;border-radius:6px;padding:8px}
.monitor-screen .video{width:100%;height:100%;background:linear-gradient(135deg,#5c6c8a,#a6473f 60%,#c9c9c9)}
.monitor-stand{left:350px;top:569px;width:56px;height:44px;background:linear-gradient(180deg,#cfcfcf,#9d9d9d);clip-path:polygon(30% 0,70% 0,100% 100%,0 100%)}
.strap-copy{left:505px;top:446px;width:420px;font-style:italic;font-size:16px;line-height:24px;color:#222}
.strap-copy strong{color:var(--red);font-weight:900}
.field{height:24px;background:var(--white);border:1px solid #cfcfcf;font-size:11px;color:#aaa;font-style:italic;padding:0 8px;line-height:22px;display:flex;justify-content:space-between}
.field svg{margin-top:6px}
.btn{background:var(--red);color:var(--white);font-weight:900;font-size:12px;text-align:center;line-height:24px;height:25px}
.promise{left:505px;top:602px;font-size:10px;color:#ccc;font-style:italic}
.social{display:flex;gap:6px}
.social span{width:26px;height:26px;display:block;border-radius:3px}

/* section headers */
.sec-head{height:24px;background:linear-gradient(180deg,#f0f0f0,#dcdcdc);font-size:11px;font-weight:900;color:#333;line-height:24px;padding-left:8px;letter-spacing:.4px}
.sec-head::after{content:"";position:absolute;left:16px;top:24px;border:5px solid transparent;border-top-color:#dcdcdc}

/* blog posts */
.post{left:226px;width:496px;text-align:center}
.post-art{margin:0 auto;width:440px;height:236px;position:relative;overflow:hidden;text-align:left}
.post-art .photo{position:absolute;right:22px;bottom:0;width:140px;height:200px;border-radius:60px 60px 0 0}
.art-text{position:absolute;left:22px;color:var(--white);font-weight:900;text-transform:uppercase;letter-spacing:1px}
.post-title{margin-top:14px;font-weight:900;font-style:italic;font-size:14px;color:#222}
.post-meta{margin-top:6px;font-size:9px;color:#888}
.post-meta b{color:var(--red);font-style:italic;border-bottom:2px solid var(--red);padding-bottom:3px}
.post-meta i{display:inline-block;width:1px;height:9px;background:#bbb;margin:0 10px;vertical-align:middle}
.post-excerpt{margin:10px auto 0;width:430px;font-size:9.5px;line-height:13px;color:#777}
.read-more{margin-top:10px;font-size:11px;color:var(--red)}
.read-more::after{content:"";display:inline-block;width:11px;height:11px;border-radius:50%;background:var(--red);margin-left:5px;vertical-align:middle}
.divider{left:226px;width:496px;height:30px}
.divider::before{content:"";position:absolute;left:0;right:0;top:15px;border-top:1px dashed #ccc}
.divider::after{content:"";position:absolute;left:234px;top:2px;width:28px;height:28px;border-radius:50%;background:var(--white);border:1px solid #ccc}

.pager{left:402px;top:1977px;display:flex;gap:6px}
.pager span{width:22px;height:22px;border-radius:50%;border:1px solid #bbb;font-size:10px;text-align:center;line-height:20px;color:#666}
.pager span.on{border-color:var(--red);color:var(--red)}

/* sidebar */
.side{left:745px;width:230px}
.pop-item{position:absolute;left:10px;width:210px;height:52px;display:flex;gap:10px;border-bottom:1px solid #eee}
.pop-thumb{width:58px;height:46px;flex:none}
.pop-title{font-size:10px;line-height:13px;color:#333}
.pop-date{font-size:8px;color:var(--red);margin-top:3px}
.view-all{font-size:9px;font-weight:700;color:#333;border-bottom:2px solid var(--red);padding-bottom:2px}
.tags{left:754px;top:1146px;width:214px;display:flex;flex-wrap:wrap;gap:4px;justify-content:center}
.tag{background:var(--red);color:var(--white);font-size:11px;padding:4px 6px;line-height:14px}
.tag.big{font-size:19px;line-height:22px;padding:2px 6px}
.tag.dark{background:#2a2a2a}
.promo{left:756px;top:1414px;width:210px;height:454px;background:linear-gradient(180deg,#333 0%,#4a4a4a 55%,#2a2a2a 100%);overflow:hidden}
.promo-head{position:absolute;left:12px;top:10px;color:var(--white);font-weight:900;font-size:19px;line-height:23px;letter-spacing:.5px}
.promo-band{position:absolute;left:0;top:300px;width:210px;height:106px;background:var(--red);text-align:center;color:var(--white)}
.promo-live{font-weight:900;font-size:46px;line-height:52px;letter-spacing:3px;margin-top:6px}
.promo-places{font-size:13px;font-style:italic}
.promo-places b{font-size:18px}
.promo-btn{position:absolute;left:48px;top:392px;width:114px;height:26px;background:var(--red-dark);color:var(--white);font-weight:900;font-size:11px;text-align:center;line-height:26px;border:2px solid var(--white)}

/* newsletter + footer */
.newsletter{left:0;top:2037px;width:1200px;height:174px;background:linear-gradient(180deg,#f1f1f1,#e3e3e3)}
.newsletter-copy{left:300px;top:2072px;width:600px;text-align:center;font-style:italic;font-size:16px;line-height:25px;color:#222}
.footer{left:0;top:2211px;width:1200px;height:45px;background:var(--red)}
.footer-legal{left:240px;top:2226px;color:var(--white);font-size:9px;display:flex;gap:22px;letter-spacing:.3px}
</style>
</head>
<body>

<header class="abs topbar">
  <div class="abs brand"><span class="brand-dot"></span>Marla Penrick</div>
  <nav class="abs menu">
    <a class="active" href="#">EVENTS</a>
    <a href="#">WORK WITH ME</a>
    <a href="#">CORPORATE</a>
    <a href="#">ABOUT</a>
    <a href="#">CONTACT</a>
  </nav>
</header>

<section class="abs hero">
  <div class="abs hero-photo" role="img" aria-label="Photo of Marla in a red dress, hands on hips"></div>
  <div class="abs hero-word red" style="top:96px">ATTRACT</div>
  <div class="abs hero-rule" style="left:372px;top:162px;width:305px"></div>
  <div class="abs hero-word" style="top:169px">CONNECT</div>
  <div class="abs hero-rule" style="left:226px;top:236px;width:315px"></div>
  <div class="abs hero-word red" style="top:243px">INFLUENCE</div>
</section>

<section class="abs strap"></section>
<div class="abs strap-black"></div>
<div class="abs monitor-screen"><div class="video" role="img" aria-label="Free training video preview"></div></div>
<div class="abs monitor-stand"></div>
<p class="abs strap-copy">Learn how to unlock the superpower* of your charisma and win all the business you want with this <strong>FREE</strong> training.</p>
<div class="abs field" style="left:505px;top:508px;width:179px">First name
  <svg width="10" height="10" viewBox="0 0 10 10"><circle cx="5" cy="3" r="2.4" fill="#999"/><path d="M0 10c0-3 2-5 5-5s5 2 5 5z" fill="#999"/></svg></div>
<div class="abs field" style="left:693px;top:508px;width:176px">Email address
  <svg width="11" height="9" viewBox="0 0 11 9"><rect x=".5" y=".5" width="10" height="8" fill="none" stroke="#999"/><path d="M.5 .5l5 4 5-4" fill="none" stroke="#999"/></svg></div>
<div class="abs btn" style="left:767px;top:543px;width:102px">YES PLEASE!</div>
<p class="abs promise">* Promise to only use your powers for good</p>
<div class="abs social" style="left:794px;top:597px" aria-label="Social links">
  <span style="background:#3aa8e0"></span><span style="background:#3b5a99"></span><span style="background:#1f7bb6"></span><span style="background:#c8232c"></span><span style="background:#7a5a45"></span>
</div>

<!-- blog column -->
<div class="abs sec-head" style="left:226px;top:661px;width:496px">BLOG</div>

<article class="abs post" style="top:713px">
  <div class="post-art" style="background:var(--coral)">
    <div class="photo" style="background:linear-gradient(180deg,#b9897a,#d8332f)" role="img" aria-label="Marla presenting with a microphone"></div>
    <div class="art-text" style="top:78px;font-size:24px">Public speaking...</div>
    <div class="art-text" style="top:134px;font-size:30px;text-transform:none">Made Easy :-)</div>
  </div>
  <h2 class="post-title">Public speaking...made easy</h2>
  <p class="post-meta">by <b>Marla Penrick</b><i></i>July 22, 2016</p>
  <p class="post-excerpt">Lorem ipsum dolor sit amet, consectetur adipiscing elit. Praesent fringilla tortor et mi convallis, ut scelerisque dui rhoncus. Donec quis lorem malesuada, molestie metus id, vehicula lacus. Pellentesque ultricies venenatis ullamcorper. Sed metus ligula, pharetra id risus eu, fermentum auctor eros.</p>
  <p class="read-more">Read More</p>
</article>
<div class="abs divider" style="top:1093px"></div>

<article class="abs post" style="top:1144px">
  <div class="post-art" style="background:var(--green)">
    <div class="photo" style="background:linear-gradient(180deg,#8a6a5a,#2c4d8f)" role="img" aria-label="Marla smiling, wearing glasses"></div>
    <div class="art-text" style="top:20px;font-size:22px;line-height:30px">How to start every day<br>in the right frame<br>of mind!</div>
    <div class="art-text" style="top:176px;font-size:24px">5 hot tips</div>
  </div>
  <h2 class="post-title">How to start every day in the right frame of mind!</h2>
  <p class="post-meta">by <b>Marla Penrick</b><i></i>July 22, 2016</p>
  <p class="post-excerpt">Lorem ipsum dolor sit amet, consectetur adipiscing elit. Praesent fringilla tortor et mi convallis, ut scelerisque dui rhoncus. Donec quis lorem malesuada, molestie metus id, vehicula lacus. Pellentesque ultricies venenatis ullamcorper. Sed metus ligula, pharetra id risus eu, fermentum auctor eros.</p>
  <p class="read-more">Read More</p>
</article>
<div class="abs divider" style="top:1526px"></div>

<article class="abs post" style="top:1572px">
  <div class="post-art" style="background:var(--cyan)">
    <div class="photo" style="background:linear-gradient(180deg,#9a7666,#333)" role="img" aria-label="Marla in glasses, looking thoughtful"></div>
    <div class="abs" style="left:228px;top:18px;width:100px;height:100px;border-radius:50%;background:var(--white)" role="img" aria-label="Red dress and shoes sketch"></div>
    <div class="art-text" style="top:20px;font-size:22px;line-height:30px">Take charge<br>of your<br>style...</div>
    <div class="art-text" style="top:150px;font-size:24px;line-height:32px">...boost your<br>confidence</div>
  </div>
  <h2 class="post-title">Take charge of your style...Boost your confidence</h2>
  <p class="post-meta">by <b>Marla Penrick</b><i></i>July 22, 2016</p>
  <p class="post-excerpt">Lorem ipsum dolor sit amet, consectetur adipiscing elit. Praesent fringilla tortor et mi convallis, ut scelerisque dui rhoncus. Donec quis lorem malesuada, molestie metus id, vehicula lacus. Pellentesque ultricies venenatis ullamcorper. Sed metus ligula, pharetra id risus eu, fermentum auctor eros.</p>
  <p class="read-more">Read More</p>
</article>

<nav class="abs pager">
  <span>&lsaquo;</span><span class="on">1</span><span>2</span><span>3</span><span>4</span><span>&rsaquo;</span>
</nav>

<!-- sidebar -->
<div class="abs sec-head side" style="top:661px">POPULER</div>
<div class="abs side" style="top:700px;height:360px">
  <div class="pop-item" style="top:0"><div class="pop-thumb" style="background:#3a82c4" role="img" aria-label="Style post thumbnail"></div><div><p class="pop-title">Take charge of your style...</p><p class="pop-date">July 22, 2016</p></div></div>
  <div class="pop-item" style="top:58px"><div class="pop-thumb" style="background:#e0a21f" role="img" aria-label="Fulfilment post thumbnail"></div><div><p class="pop-title">Unfulfilled? It's time to think about your...</p><p class="pop-date">July 22, 2016</p></div></div>
  <div class="pop-item" style="top:116px"><div class="pop-thumb" style="background:#3b2a22" role="img" aria-label="Confidence post thumbnail"></div><div><p class="pop-title">...Boost your confidence</p><p class="pop-date">July 22, 2016</p></div></div>
  <div class="pop-item" style="top:174px"><div class="pop-thumb" style="background:var(--cyan)" role="img" aria-label="Style post thumbnail"></div><div><p class="pop-title">Take charge of your style...</p><p class="pop-date">July 22, 2016</p></div></div>
  <div class="pop-item" style="top:232px"><div class="pop-thumb" style="background:var(--coral)" role="img" aria-label="Public speaking post thumbnail"></div><div><p class="pop-title">Public speaking... made easy</p><p class="pop-date">July 22, 2016</p></div></div>
  <div class="pop-item" style="top:290px"><div class="pop-thumb" style="background:var(--green)" role="img" aria-label="Frame of mind post thumbnail"></div><div><p class="pop-title">How to start every day in the right frame...</p><p class="pop-date">July 22, 2016</p></div></div>
</div>
<div class="abs" style="left:840px;top:1066px"><span class="view-all">VIEW ALL</span></div>

<div class="abs sec-head side" style="top:1112px">TAGS</div>
<div class="abs tags">
  <span class="tag">nlp</span><span class="tag">body language</span>
  <span class="tag big">capsule wardrobe</span>
  <span class="tag">confidence</span><span class="tag dark">handshake</span><span class="tag">mindset</span>
  <span class="tag">passion</span><span class="tag big">power pose</span>
  <span class="tag">presentations</span><span class="tag">presence</span>
  <span class="tag big">rapport</span><span class="tag">spring wear</span><span class="tag">style</span>
  <span class="tag">values</span><span class="tag">vision board</span><span class="tag">warmth</span>
</div>

<div class="abs sec-head side" style="top:1369px">COMMING UP</div>
<div class="abs promo" role="img" aria-label="Live event promo photo of Marla on stage">
  <div class="promo-head">UNLOCK<br>THE<br>SUPERPOWER<br>OF CHARISMA</div>
  <div class="promo-band">
    <div class="promo-live">LIVE</div>
    <div class="promo-places">*Only <b>6</b> places left.</div>
  </div>
  <div class="promo-btn">LEARN MORE</div>
</div>

<!-- newsletter -->
<section class="abs newsletter"></section>
<p class="abs newsletter-copy">Hey! Don't go without signing up because you'll miss out on exclusive offers, awesome tips, and weekly motivation in my fab newsletter *.</p>
<div class="abs field" style="left:360px;top:2138px;width:176px">First name
  <svg width="10" height="10" viewBox="0 0 10 10"><circle cx="5" cy="3" r="2.4" fill="#999"/><path d="M0 10c0-3 2-5 5-5s5 2 5 5z" fill="#999"/></svg></div>
<div class="abs field" style="left:548px;top:2138px;width:176px">Email address
  <svg width="11" height="9" viewBox="0 0 11 9"><rect x=".5" y=".5" width="10" height="8" fill="none" stroke="#999"/><path d="M.5 .5l5 4 5-4" fill="none" stroke="#999"/></svg></div>
<div class="abs btn" style="left:738px;top:2137px;width:102px">YES PLEASE!</div>

<footer class="abs footer"></footer>
<div class="abs footer-legal"><span>© 2016 Marla Penrick Ltd</span><span>PRIVACY POLICY</span><span>TERMS POLICY</span><span>DISCLAIMERS</span></div>
<div class="abs social" style="left:794px;top:2220px" aria-label="Social links">
  <span style="background:#3aa8e0"></span><span style="background:#3b5a99"></span><span style="background:#1f7bb6"></span><span style="background:#c8232c"></span><span style="background:#7a5a45"></span>
</div>

</body>
</html>
```